Corbrook Estates LLC stationary for a real estate property management company.

Create stationary (letterhead, envelopes, business cards) using Corbrook Estates LLC logo as primary creative element. Stationary design needs to be horizontal, leaving as much space as possible for correspondence copy. See attached Creative Brief and past stationary files for details.

Target Market(s)

Prospective apartment residents and current residents, vendors, and government agencies.

Industry/Entity Type

Property Management

Contact Information for Business Card

Business card employee title: Property Manager. Should include address, phone, fax, email, website, slogan, and Corbrook Estates logo.

Font styles to use
Sans Serif

Colors
0592cd
000000

Requirements
Must have
• Tone should be conservative, institutional, business (i.e. banking, finance, real estate). Must include: address, phone, fax, website, and slogan (see attached Creative Brief). Should be a horizontal design, leaving as much room as possible for letter correspondence copy.
Nice to have
• Please use an Arial or Helvetica style font.
Should not have
• Letterhead layout should leave as much room as possible for copy.

```html
<!DOCTYPE html>
<html lang="en">
<head>
<meta charset="utf-8">
<title>Corbrook Estates LLC – Letterhead</title>
<link href="https://fonts.googleapis.com/css2?family=Raleway:wght@400;500;700&display=swap" rel="stylesheet">
<style>
  :root {
    --brand-blue: #0a5699;
    --ink: #1a1a1a;
    --paper: #ffffff;
    --frame: #222222;
  }
  * { margin: 0; padding: 0; box-sizing: border-box; }
  html, body {
    width: 849px; height: 1200px; overflow: hidden;
    background: var(--paper);
  }
  .letterhead {
    position: relative;
    width: 849px; height: 1200px;
    background: var(--paper);
    border: 1px solid var(--frame);
    font-family: "Raleway", Arial, sans-serif;
  }
  .brand {
    position: absolute;
    left: 34px; top: 26px;
    display: flex; align-items: flex-start; gap: 16px;
  }
  .brand-mark {
    width: 62px; height: 62px;
    background: var(--brand-blue);
    margin-top: 8px;
  }
  .brand-text { padding-top: 14px; }
  .brand-name {
    color: var(--brand-blue);
    font-weight: 700;
    font-size: 21px;
    line-height: 25px;
    letter-spacing: 3px;
    text-transform: uppercase;
  }
  .brand-tagline {
    margin-top: 8px;
    color: var(--ink);
    font-weight: 500;
    font-size: 11.5px;
    letter-spacing: 0.2px;
    text-transform: uppercase;
    white-space: nowrap;
  }
  .contact-panel {
    position: absolute;
    left: 421px; top: 0;
    width: 387px; height: 145px;
    background: var(--brand-blue);
    padding: 29px 0 0 16px;
    list-style: none;
  }
  .contact-item {
    display: flex; align-items: center;
    height: 21.5px;
    color: var(--paper);
    font-size: 15.5px;
    font-weight: 400;
    letter-spacing: -0.3px;
    white-space: nowrap;
  }
  .contact-icon {
    width: 15px; height: 15px;
    margin-right: 17px;
    fill: var(--paper);
    flex: none;
  }
</style>
</head>
<body>
  <main class="letterhead">
    <header>
      <div class="brand">
        <div class="brand-mark"></div>
        <div class="brand-text">
          <div class="brand-name">Corbrook<br>Estates LLC</div>
          <div class="brand-tagline">Multifamily Property Management</div>
        </div>
      </div>

      <ul class="contact-panel">
        <li class="contact-item">
          <svg class="contact-icon" viewBox="0 0 16 16" aria-hidden="true">
            <path d="M8 0.5a5 5 0 0 0-5 5c0 3.6 5 10 5 10s5-6.4 5-10a5 5 0 0 0-5-5zm0 7a2 2 0 1 1 0-4 2 2 0 0 1 0 4z"/>
          </svg>
          2680 Harbor Rd. #310, San Diego, CA 92110
        </li>
        <li class="contact-item">
          <svg class="contact-icon" viewBox="0 0 16 16" aria-hidden="true">
            <path d="M3.6 1.2l2.2 2.6c.3.4.3.9 0 1.3L4.9 6.3c.8 1.8 2.5 3.6 4.6 4.7l1.2-1c.4-.3.9-.3 1.3 0l2.5 2.1c.4.4.4 1 0 1.4l-1.3 1.2c-.6.5-1.5.6-2.3.3C6.6 13.4 3 9.8 1.4 5.5c-.3-.8-.1-1.7.5-2.3L3 1.2c.2-.2.5-.2.6 0z"/>
          </svg>
          858-555-0142
        </li>
        <li class="contact-item">
          <svg class="contact-icon" viewBox="0 0 16 16" aria-hidden="true">
            <path d="M4 1h6l2 2v3H4zM1.5 7h13v6h-2.5v-2H4v2H1.5zM5 12h6v3H5z"/>
          </svg>
          858-555-0187
        </li>
        <li class="contact-item">
          <svg class="contact-icon" viewBox="0 0 16 16" aria-hidden="true">
            <g fill="none" stroke="#ffffff" stroke-width="1.3">
              <circle cx="8" cy="8" r="6.6"/>
              <ellipse cx="8" cy="8" rx="2.8" ry="6.6"/>
              <path d="M1.4 8h13.2M2.4 4.6h11.2M2.4 11.4h11.2"/>
            </g>
          </svg>
          www.corbrookestates.us
        </li>
      </ul>
    </header>
  </main>
</body>
</html>
```